Commercial Real Estate Company Needs an Awesome Flyer Design for their Oceanfront Property

We need a 2-page flyer or our Class A Oceanfront Property in Santa Monica, California. Approximately 16,149 square feet of Class A rare oceanfront office space with private balconies will be in available 4th Quarter of 2014. The SPACE has not been on the market for over 20 YEARS!

I attached our Previous 2-page flyer for the 2,353 square feet. We need a new vibrant, modern flyer that will attract Tech, Entertainment, Financial, and Marketing Companies to our building. Also, the 2nd Floor Space Plan is attached.

Also, please check out our website www.velabrookproperties.com. We would like to use the colors of our website and logo to incorporate with the flyer.

I updated the Must Have's on the Listing!

Target Market(s)

Entertainment, Financial, Tech Companies

Industry/Entity Type

Real Estate

Requirements
Must have
• Our Company Logo, Company, Leasing Agents On the First and 2nd Page

Dustin R. Hallorann (310) 555-0142
dusty@velabrookproperties.com

Owen Tu (310) 555-0187
owen@velabrookproperties.com

Velabrook Properties.
5172 E Harlow Ave, Suite 414
West Hollywood, Ca. 90069
(310) 555-0142
www.velabrookproperties.com

Also, the Front Page should indicate

"Rare Class A Oceanfront Office Space in the heart of Santa Monica"
"2nd Floor Office Space consisting of 16,159 square feet with private balconies."
Nice to have
• Please use description of the office building. You can omit whatever you think is unnecessary

"Bellwether Court is one of Santa Monica's rare commercial properties that is both strategically located in the city's burgeoning central business district, yet ideally positioned on palm-lined Ocean Ave directly across from the Pacific Ocean. Built in 1987, the 3-story mixed-use commercial and retail property features prestigious retail Tenants such as Kelp Haus and Tidal Oven."

"A year-round coastal Mediterranean climate, a highly diverse business sector, and the vibrant, pedestrian-oriented Linden Row Arcade and Marigold Commons makes this beachside community a highly desirable commercial and retail location."

```html
<!DOCTYPE html>
<html lang="en">
<head>
<meta charset="utf-8">
<title>Bellwether Court – Leasing Flyer</title>
<link rel="stylesheet" href="https://fonts.googleapis.com/css2?family=Cinzel:wght@400&family=Open+Sans:wght@400;600&family=Pinyon+Script&display=swap">
<style>
  :root {
    --ink: #231f20;
    --gold: #fdd327;
    --gold-deep: #f5c518;
    --mist: #d6d7d9;
    --text: #3d3d3d;
    --quote: #9a9278;
    --white: #ffffff;
  }
  * { margin: 0; padding: 0; box-sizing: border-box; }
  html, body { width: 1200px; height: 792px; overflow: hidden; background: var(--white); }
  body { position: relative; font-family: "Open Sans", Arial, sans-serif; color: var(--text); }

  .page { position: absolute; top: 13px; width: 542px; height: 766px; background: var(--mist); overflow: hidden; }
  .page--front { left: 38px; }
  .page--back { left: 617px; }

  .masthead { position: absolute; left: 0; top: 0; width: 100%; height: 67px; background: var(--ink); }
  .masthead__title { position: absolute; left: 0; right: 0; top: 16px; text-align: center; font-family: "Cinzel", Georgia, serif; font-weight: 400; font-size: 30px; color: var(--gold); letter-spacing: 0.3px; }
  .brand { position: absolute; top: 10px; width: 50px; height: 48px; background: var(--white); display: flex; flex-direction: column; align-items: center; justify-content: center; gap: 4px; }
  .brand--left { left: 12px; }
  .brand--right { right: 12px; }
  .brand__dot { width: 14px; height: 14px; border-radius: 50%; background: var(--ink); }
  .brand__name { font-size: 6px; font-weight: 600; color: var(--ink); letter-spacing: 0.4px; }

  .photo { position: absolute; }
  .photo--hero { left: 0; top: 67px; width: 542px; height: 302px; background: linear-gradient(180deg, #2f55a6 0%, #6f8fc6 30%, #d9d6d2 50%, #c9c2ba 68%, #3b3d44 80%, #8a8c91 100%); }
  .thumb { position: absolute; top: 378px; height: 126px; border: 1.5px solid var(--gold-deep); }
  .thumb--room { left: 12px; width: 190px; background: linear-gradient(180deg, #cfc8b8 0%, #b9ad97 60%, #5a4e40 100%); }
  .thumb--plan { left: 213px; width: 118px; background: #f4f4f2; }
  .thumb--open { left: 342px; width: 189px; background: linear-gradient(180deg, #e6e1d6 0%, #c9b898 55%, #a77a45 100%); }

  .feature { position: absolute; left: 0; top: 522px; width: 100%; height: 166px; background: var(--gold); }
  .feature__headline { position: absolute; left: 12px; top: 4px; font-family: "Pinyon Script", cursive; font-size: 58px; color: var(--ink); white-space: nowrap; }
  .feature__quote { position: absolute; font-family: Georgia, serif; font-size: 58px; font-weight: 700; color: var(--quote); line-height: 1; }
  .feature__quote--open { left: 10px; top: 80px; }
  .feature__quote--close { right: 12px; top: 126px; }
  .feature__lines { position: absolute; left: 55px; top: 100px; width: 440px; font-size: 12px; color: var(--ink); line-height: 23px; white-space: nowrap; }

  .agents-strip { position: absolute; left: 42px; right: 50px; top: 707px; font-size: 10px; color: var(--ink); }
  .agents-strip__label { text-align: center; font-size: 10.5px; padding-bottom: 3px; border-bottom: 1px solid #9a9a9a; }
  .agents-strip__row { display: flex; justify-content: space-between; margin-top: 5px; line-height: 13px; }

  .section-head { position: absolute; height: 20px; display: flex; }
  .section-head__mark { width: 25px; height: 20px; background: var(--ink); }
  .section-head__tab { height: 20px; width: 172px; background: var(--gold); clip-path: polygon(0 0, 88% 0, 100% 100%, 0 100%); font-size: 12.5px; color: var(--ink); padding-left: 12px; line-height: 20px; }
  .copy { position: absolute; font-size: 8.4px; line-height: 11.8px; text-align: justify; color: var(--text); }
  .points { position: absolute; list-style: none; font-size: 8.4px; line-height: 10.8px; color: var(--text); }
  .points li { position: relative; padding-left: 22px; }
  .points li::before { content: "✸"; position: absolute; left: 0; top: 4px; font-size: 9px; color: var(--ink); }

  .photo--lobby { left: 320px; top: 306px; width: 230px; height: 134px; border: 2px solid var(--white); background: linear-gradient(90deg, #8b8c90 0%, #56585c 40%, #9c9a98 75%, #8d2a2a 100%); }
  .tagline { position: absolute; left: 320px; top: 490px; width: 222px; font-family: "Pinyon Script", cursive; font-size: 36px; line-height: 46px; color: var(--ink); text-align: center; }

  .footer { position: absolute; left: 0; top: 635px; width: 100%; height: 131px; background: var(--gold); }
  .footer__block { position: absolute; top: 29px; font-size: 6.8px; line-height: 10.8px; color: #6b5a1a; }
  .footer__block--contact { left: 61px; }
  .footer__block--agents { left: 320px; top: 28px; }
  .footer__title { font-size: 10.5px; color: var(--ink); margin-bottom: 3px; }
  .footer__line { display: flex; align-items: center; gap: 6px; }
  .footer__line svg { width: 7px; height: 7px; flex: none; }
  .footer__indent { padding-left: 13px; }
</style>
</head>
<body>

<section class="page page--front">
  <header class="masthead">
    <div class="brand brand--left"><span class="brand__dot"></span><span class="brand__name">VELABROOK</span></div>
    <h1 class="masthead__title">BELLWETHER COURT</h1>
    <div class="brand brand--right"><span class="brand__dot"></span><span class="brand__name">VELABROOK</span></div>
  </header>

  <div class="photo photo--hero" role="img" aria-label="Exterior photo of the three-story white building with palm trees and street-level retail under a blue sky"></div>
  <div class="thumb thumb--room" role="img" aria-label="Empty office interior with windows overlooking palms"></div>
  <div class="thumb thumb--plan" role="img" aria-label="Second floor space plan"></div>
  <div class="thumb thumb--open" role="img" aria-label="Open office area with curved wood reception desk"></div>

  <div class="feature">
    <div class="feature__headline">Prestigious Workplace</div>
    <span class="feature__quote feature__quote--open">“</span>
    <p class="feature__lines">Rare Class A Oceanfront Office Space in the heart of Santa Monica.<br>2nd Floor Office Space consisting of 16,159 square feet with private balconies.</p>
    <span class="feature__quote feature__quote--close">”</span>
  </div>

  <div class="agents-strip">
    <div class="agents-strip__label">Our Leasing Agents :</div>
    <div class="agents-strip__row">
      <div>Dustin R. Hallorann (310) 555-0142<br>dusty@velabrookproperties.com</div>
      <div>Owen Tu (310) 555-0187<br>owen@velabrookproperties.com</div>
    </div>
  </div>
</section>

<section class="page page--back">
  <header class="masthead">
    <div class="brand brand--left"><span class="brand__dot"></span><span class="brand__name">VELABROOK</span></div>
    <h1 class="masthead__title">BELLWETHER COURT</h1>
    <div class="brand brand--right"><span class="brand__dot"></span><span class="brand__name">VELABROOK</span></div>
  </header>

  <div class="section-head" style="left:35px; top:99px;"><span class="section-head__mark"></span><span class="section-head__tab">About Us</span></div>
  <p class="copy" style="left:35px; top:131px; width:218px;">Bellwether Court is one of Santa Monica's rare commercial properties that is both strategically located in the city's burgeoning central business district, yet ideally positioned on palm-lined Ocean Ave directly across from the Pacific Ocean. Built in 1987, the 3-story mixed-use commercial and retail property features prestigious retail Tenants such as Kelp Haus and Tidal Oven.</p>

  <div class="section-head" style="left:293px; top:99px;"><span class="section-head__mark"></span><span class="section-head__tab">Property Description</span></div>
  <p class="copy" style="left:293px; top:131px; width:218px;">A year-round coastal Mediterranean climate, a highly diverse business sector, and the vibrant, pedestrian-oriented Linden Row Arcade and Marigold Commons makes this beachside community a highly desirable commercial and retail location.</p>
  <ul class="points" style="left:301px; top:207px; width:210px;">
    <li style="margin-bottom:14px;">Rare Class A Oceanfront Office Space in the heart of Santa Monica.</li>
    <li>2nd Floor Office Space consisting of 16,159 square feet with private balconies.</li>
  </ul>

  <div class="section-head" style="left:35px; top:290px;"><span class="section-head__mark"></span><span class="section-head__tab">Building Amenities</span></div>
  <ul class="points" style="left:40px; top:333px; width:226px;">
    <li style="margin-bottom:17px;">Lorem ipsum dolor sit amet, consectetur adipiscing elit. Sed at ante.</li>
    <li style="margin-bottom:14px;">Lorem ipsum dolor sit amet, consectetur adipiscing elit. Sed at ante. Mauris eleifend, quam a vulputate dictum.</li>
    <li style="margin-bottom:18px;">Lorem ipsum dolor sit amet, consectetur adipiscing elit. Sed at ante. Mauris eleifend</li>
    <li style="margin-bottom:18px;">Lorem ipsum dolor sit amet, consectetur adipiscing elit. Sed at ante.</li>
    <li style="margin-bottom:16px;">Lorem ipsum dolor sit amet, consectetur adipiscing elit. Sed at ante. Mauris eleifend, quam a vulputate dictum.</li>
    <li>Lorem ipsum dolor sit amet, consectetur adipiscing elit. Sed at ante. Mauris eleifend, quam a vulputate dictum.</li>
  </ul>

  <div class="photo photo--lobby" role="img" aria-label="Elevator lobby with grey panelled walls and red carpet runners"></div>
  <p class="tagline">“ Your Choice,<br>Your Office ”</p>

  <footer class="footer">
    <div class="footer__block footer__block--contact">
      <div class="footer__title">Contact Us :</div>
      <div class="footer__line"><svg viewBox="0 0 10 10"><path d="M5 0a3.5 3.5 0 0 0-3.5 3.5C1.5 6 5 10 5 10s3.5-4 3.5-6.5A3.5 3.5 0 0 0 5 0zm0 5a1.5 1.5 0 1 1 0-3 1.5 1.5 0 0 1 0 3z" fill="#231f20"/></svg>Velabrook Properties.</div>
      <div class="footer__indent">5172 E Harlow Ave, Suite 414,<br>West Hollywood, Ca. 90069.</div>
      <div class="footer__line"><svg viewBox="0 0 10 10"><rect x="1" y="1" width="8" height="8" rx="1.5" fill="#231f20"/></svg>(310) 555-0142</div>
      <div class="footer__line"><svg viewBox="0 0 10 10"><rect x="0.5" y="2" width="9" height="6" fill="#231f20"/></svg>www.velabrookproperties.com</div>
    </div>
    <div class="footer__block footer__block--agents">
      <div class="footer__title">Our Leasing Agents :</div>
      <div class="footer__indent">Dustin R. Hallorann</div>
      <div class="footer__line"><svg viewBox="0 0 10 10"><rect x="1" y="1" width="8" height="8" rx="1.5" fill="#231f20"/></svg>(310) 555-0142</div>
      <div class="footer__line"><svg viewBox="0 0 10 10"><rect x="0.5" y="2" width="9" height="6" fill="#231f20"/></svg>dusty@velabrookproperties.com</div>
      <div class="footer__indent" style="margin-top:3px;">Owen Tu</div>
      <div class="footer__line"><svg viewBox="0 0 10 10"><rect x="1" y="1" width="8" height="8" rx="1.5" fill="#231f20"/></svg>(310) 555-0187</div>
      <div class="footer__line"><svg viewBox="0 0 10 10"><rect x="0.5" y="2" width="9" height="6" fill="#231f20"/></svg>owen@velabrookproperties.com</div>
    </div>
  </footer>
</section>

</body>
</html>
```